Powerpoint Presentation Makeover & Update

I have a key-note presentation coming up in a couple weeks in front of about 200 bankers. Our company Corvalen www.corvalen-fs.example has a Western theme and motif which sets our brand apart and which I would like to maintain.

I have an existing presentation (which I can provide) which I need to have "freshened" up so that the bullet point slides are more graphical and appealing without departing too much from the current design as it is pretty good.

The final design should be easy to modify as I will be adding and subtracting slides after I get the presentation back.

Target Market(s)

CEOs and CFOs of small community bank and credit unions across the U.S.

Industry/Entity Type

It Company

Requirements
Must have
• stick with the current western theme and corporate branding (logo, knight, etc.) and just expand it further and make slides more visually appealing.
Nice to have
• appropriate animation where necessary. I don't like to 'click' for every single bullet point but presenting 2-3 at a time. Observe the existing animations for an idea.
Should not have
• Just because this is a financial crowd I do not want to bore them with conservative designs. Presenting before my speech will be plenty of these types of firms.

```html
<!DOCTYPE html>
<html lang="en">
<head>
<meta charset="utf-8">
<title>Corvalen Research – Slide Overview</title>
<link rel="stylesheet" href="https://fonts.googleapis.com/css2?family=Arimo:ital,wght@0,400;0,700;1,400;1,700&display=swap">
<style>
  :root {
    --navy: #0b2a6e;
    --slide-bg: #e9eaed;
    --header-top: #ffffff;
    --header-bottom: #d5d9e0;
    --rule: #8a9bb8;
    --brand-blue: #2a5d9a;
    --mark-dark: #1c1a19;
    --title-blue: #1a64a6;
    --ink: #1b1b1b;
    --muted: #3a3a3a;
    --line-red: #8e1a38;
    --line-blue: #1f5aa0;
    --firm-blue: #1f4f9a;
    --wood-light: #d6d8da;
    --wood-mid: #b9bcc0;
    --wood-dark: #9da1a6;
  }
  * { box-sizing: border-box; margin: 0; padding: 0; }
  html, body { width: 1200px; height: 840px; overflow: hidden; }
  body { background: var(--navy); font-family: "Arimo", Arial, sans-serif; color: var(--ink); position: relative; }

  .slide { position: absolute; width: 476px; height: 266px; background: var(--slide-bg); overflow: hidden; }
  .slide.col-1 { left: 92px; } .slide.col-2 { left: 644px; }
  .slide.row-1 { top: 10px; } .slide.row-2 { top: 288px; } .slide.row-3 { top: 569px; }

  .slide-header { position: absolute; left: 0; top: 0; width: 100%; height: 30px; z-index: 2;
    background: linear-gradient(var(--header-top), var(--header-bottom));
    border-bottom: 2px solid var(--rule); }
  .brand { position: absolute; right: 8px; top: 2px; display: flex; align-items: flex-start; gap: 8px;
    color: var(--brand-blue); font-size: 17px; }
  .brand-name { margin-top: 4px; letter-spacing: 0.2px; }
  .brand-mark { width: 36px; height: 36px; border-radius: 50%; background: var(--mark-dark); }

  .slide-footer { position: absolute; left: 0; bottom: 0; width: 100%; height: 34px; border-bottom: 3px solid #c3c9d3; }
  .firm-badge { position: absolute; left: 14px; bottom: 10px; display: flex; align-items: center; gap: 5px;
    color: var(--firm-blue); font-size: 12px; font-weight: 700; }
  .firm-badge-square { width: 16px; height: 16px; background: var(--firm-blue); }
  .site-url { position: absolute; right: 24px; bottom: 10px; font-size: 10px; font-weight: 700; color: var(--brand-blue); letter-spacing: 0.3px; }

  .title-bar { position: absolute; left: 4px; width: 60px; height: 12px; background: linear-gradient(90deg, #f4f4f4, #222); }
  .slide-title { position: absolute; left: 72px; color: var(--title-blue); font-size: 19px; font-weight: 700; letter-spacing: 0.4px; white-space: nowrap; }

  ul.bullets { position: absolute; list-style: none; font-size: 9.6px; font-weight: 700; line-height: 12px; }
  ul.bullets li { position: relative; padding-left: 14px; }
  ul.bullets li::before { content: ""; position: absolute; left: 0; top: 3px; width: 6px; height: 6px; border-radius: 50%; background: var(--brand-blue); }
  .sub { display: block; font-weight: 400; font-style: italic; font-size: 8.4px; color: var(--muted); }
  .justify li { text-align: justify; }

  /* Cover */
  .cover-wood { position: absolute; inset: 30px 0 0 0;
    background: linear-gradient(90deg, var(--wood-mid), var(--wood-light) 30%, var(--wood-dark) 55%, var(--wood-light) 80%, var(--wood-mid)); }
  .cover-frame { position: absolute; left: 18px; top: 38px; width: 436px; height: 218px;
    border: 4px solid #eef0f2; border-radius: 26px; box-shadow: inset 0 0 0 2px #a9aeb5, 0 1px 2px #8b9097;
    background: radial-gradient(ellipse at center, #f4f5f6 0%, #dcdfe2 55%, #c2c6cb 100%); }
  .cover-title { position: absolute; left: 0; right: 0; top: 108px; text-align: center; color: #1b4383;
    font-size: 17px; font-weight: 700; line-height: 20px; letter-spacing: 0.4px; }
  .cover-divider { position: absolute; left: 150px; top: 168px; width: 176px; height: 1px; background: #555; }
  .cover-divider::after { content: ""; position: absolute; left: 84px; top: -3px; width: 7px; height: 7px; background: #444; transform: rotate(45deg); }
  .cover-sub { position: absolute; left: 0; right: 0; top: 190px; text-align: center; font-size: 15.5px; font-style: italic; line-height: 19px; }

  /* Presenters */
  .portrait { position: absolute; left: 133px; top: 86px; width: 94px; height: 118px; background: linear-gradient(160deg, #8a9bb0, #3b4656); border: 4px solid #fff; box-shadow: 0 0 0 1px #999; }
  .presenter { position: absolute; left: 248px; top: 112px; font-size: 11px; }
  .presenter-name { font-size: 14px; font-weight: 700; letter-spacing: 0.3px; }
  .presenter-role { font-style: italic; font-size: 10px; margin-top: 1px; margin-bottom: 12px; }
  .presenter-phone { font-weight: 700; font-size: 11.5px; margin-top: 11px; letter-spacing: 0.3px; }

  /* Logistics */
  .download { position: absolute; left: 72px; top: 49px; font-size: 8.6px; font-style: italic; }
  .download-link { display: block; margin-top: 5px; font-size: 10.4px; font-weight: 700; text-decoration: underline; color: var(--ink); }

  /* Chart */
  .chart-caption { position: absolute; left: 72px; top: 67px; font-size: 10.4px; font-weight: 700; font-style: italic; letter-spacing: 0.3px; }
  .chart { position: absolute; left: 0; top: 0; }

  /* Problem */
  .problem-photo { position: absolute; left: 73px; top: 70px; width: 171px; height: 151px; background: linear-gradient(#262626, #5a5a5a 50%, #b0b0b0); }
  .problem-quote { position: absolute; left: 84px; top: 76px; width: 154px; font-size: 9.8px; font-style: italic; font-weight: 700; color: #fff; line-height: 12px; }
</style>
</head>
<body>

<!-- Cover -->
<section class="slide col-1 row-1">
  <div class="slide-header"><div class="brand"><span class="brand-name">corvalen fs</span><span class="brand-mark"></span></div></div>
  <div class="cover-wood" role="img" aria-label="Weathered grey wood plank texture"></div>
  <div class="cover-frame" role="img" aria-label="Ornate silver western frame"></div>
  <h1 class="cover-title">Repositioning Core &amp; IT Agreements<br>to Benefit Shareholders</h1>
  <div class="cover-divider"></div>
  <p class="cover-sub">Corvalen Research and<br>Market Intelligence</p>
</section>

<!-- Presenters -->
<section class="slide col-2 row-1">
  <div class="slide-header"><div class="brand"><span class="brand-name">corvalen fs</span><span class="brand-mark"></span></div></div>
  <span class="title-bar" style="top:47px"></span>
  <h2 class="slide-title" style="top:41px">Today’s Presenters</h2>
  <div class="portrait" role="img" aria-label="Portrait photo of the presenter"></div>
  <div class="presenter">
    <div class="presenter-name">Daniel R. Hale</div>
    <div class="presenter-role">President, Corvalen fs, LLC</div>
    <div>dhale@corvalen-fs.example</div>
    <div class="presenter-phone">800.555.0142 x210</div>
  </div>
  <div class="slide-footer">
    <div class="firm-badge"><span class="firm-badge-square"></span>HARLOW</div>
    <span class="site-url">www.corvalen-fs.example</span>
  </div>
</section>

<!-- Logistics -->
<section class="slide col-1 row-2">
  <div class="slide-header"><div class="brand"><span class="brand-name">corvalen fs</span><span class="brand-mark"></span></div></div>
  <span class="title-bar" style="top:54px"></span>
  <p class="download">Today’s presentation can be downloaded at:
    <span class="download-link">http://www.harlowco.example/news/webinar_library</span></p>
  <ul class="bullets" style="left:72px;top:96px;width:176px">
    <li style="margin-bottom:12px">Today’s presentation will last approximately 45 minutes.</li>
    <li style="margin-bottom:14px">We will then have time<br>for Q &amp; A.</li>
    <li>Please send your questions in using the “questions box” located on the webinar’s control panel.</li>
  </ul>
  <ul class="bullets justify" style="left:260px;top:96px;width:192px">
    <li style="margin-bottom:12px">Our audience will be muted during the session.</li>
    <li>To communicate with me during the presentation, please use the “chat box,” located on the webinar’s control panel.</li>
  </ul>
  <div class="slide-footer">
    <div class="firm-badge"><span class="firm-badge-square"></span>HARLOW</div>
    <span class="site-url">www.corvalen-fs.example</span>
  </div>
</section>

<!-- Research chart -->
<section class="slide col-2 row-2">
  <div class="slide-header"><div class="brand"><span class="brand-name">corvalen fs</span><span class="brand-mark"></span></div></div>
  <span class="title-bar" style="top:47px"></span>
  <h2 class="slide-title" style="top:41px">Corvalen National Research</h2>
  <p class="chart-caption">Core &amp; IT Non-Interest Expense vs. Fair Market Value</p>
  <svg class="chart" width="476" height="266" viewBox="0 0 476 266">
    <rect x="96" y="88" width="294" height="145" fill="#fff" stroke="#c9ced6"/>
    <path d="M114 194 C170 184 210 180 240 162 S320 120 356 114" fill="none" stroke="var(--line-red)" stroke-width="4.5"/>
    <path d="M356 114 L374 107" stroke="var(--line-red)" stroke-width="3" stroke-dasharray="4 3"/>
    <path d="M114 202 C170 192 230 178 290 168 S340 160 356 158" fill="none" stroke="var(--line-blue)" stroke-width="3.5"/>
    <path d="M356 158 L372 156" stroke="var(--line-blue)" stroke-width="2.5" stroke-dasharray="4 3"/>
    <rect x="96" y="131" width="13" height="6" fill="var(--line-blue)"/>
    <text x="114" y="137" font-size="6.4" font-weight="700" fill="var(--line-blue)" font-family="Arimo, Arial, sans-serif">Demand for Outsourcing</text>
    <rect x="96" y="152" width="13" height="6" fill="var(--line-red)"/>
    <text x="114" y="158" font-size="6.4" font-weight="700" fill="var(--line-red)" font-family="Arimo, Arial, sans-serif">Core &amp; IT Expenses (NIE) Paid</text>
    <g font-size="6.6" font-weight="700" font-family="Arimo, Arial, sans-serif" fill="#222" text-anchor="middle">
      <text x="135" y="226">1991-1995</text><text x="187" y="226">1996-2000</text>
      <text x="251" y="226">2001-2005</text><text x="308" y="226">2006-2010</text><text x="363" y="226">2011-2013</text>
    </g>
  </svg>
  <div class="slide-footer">
    <div class="firm-badge"><span class="firm-badge-square"></span>HARLOW</div>
    <span class="site-url">www.corvalen-fs.example</span>
  </div>
</section>

<!-- About -->
<section class="slide col-1 row-3">
  <div class="slide-header"><div class="brand"><span class="brand-name">corvalen fs</span><span class="brand-mark"></span></div></div>
  <span class="title-bar" style="top:46px"></span>
  <h2 class="slide-title" style="top:40px">About Harlow &amp; Associates, P.C.</h2>
  <ul class="bullets" style="left:72px;top:80px;width:176px">
    <li style="margin-bottom:12px">Established in 1911</li>
    <li style="margin-bottom:12px">Provide our clients with Assurance, Tax, Business Consulting and Risk Management Services.</li>
    <li>Offices Located in:
      <span class="sub">- Boston, MA</span><span class="sub">- Springfield, MA</span><span class="sub">- Albany, NY</span></li>
  </ul>
  <ul class="bullets" style="left:260px;top:80px;width:190px">
    <li style="margin-bottom:12px">Over 180 professionals, 45 risk management professionals.</li>
    <li>Provide services to nearly 250 financial institutions in 19 states.
      <span class="sub">- IT Assurance</span><span class="sub">- Internal Audit</span>
      <span class="sub">- Regulatory Compliance</span><span class="sub">- HarlowGRC® Integrated Risk</span></li>
  </ul>
  <div class="slide-footer">
    <div class="firm-badge"><span class="firm-badge-square"></span>HARLOW</div>
    <span class="site-url">www.corvalen-fs.example</span>
  </div>
</section>

<!-- Business problem -->
<section class="slide col-2 row-3">
  <div class="slide-header"><div class="brand"><span class="brand-name">corvalen fs</span><span class="brand-mark"></span></div></div>
  <span class="title-bar" style="top:47px"></span>
  <h2 class="slide-title" style="top:41px">Business Problem</h2>
  <div class="problem-photo" role="img" aria-label="Black and white rodeo photo of a rider on a bucking animal"></div>
  <p class="problem-quote">Bank leaders have no reliable way to understand what they should be paying these service providers</p>
  <ul class="bullets" style="left:263px;top:68px;width:186px">
    <li style="margin-bottom:10px">Massive consolidation has led to few remaining choices and lack of innovation.</li>
    <li style="margin-bottom:10px">RFPs are antagonistic, a waste of time and $ if used as a tactic to extract cost savings.</li>
    <li style="margin-bottom:10px">Bankers have little time to spend haggling with vendors.</li>
    <li>Bankers lack the inside vendor knowledge and expertise</li>
  </ul>
  <div class="slide-footer">
    <div class="firm-badge"><span class="firm-badge-square"></span>HARLOW</div>
    <span class="site-url">www.corvalen-fs.example</span>
  </div>
</section>

</body>
</html>
```